Briefpapier, Visitenkarten, Bindemappe, Brieumschläge....
Zielgruppe
Steuerberatung vorwiegen für Unternehmer
Aufgabenstellung
Ein Logo ist bereits vorhanden (siehe Analgen) kann aber gerne auch bei einer guten Idee modernisiert werden. Ganz ein neues Logo möchte ich meinen Kunden jedoch ersparen, da ich es erst von zwei Jahren gewechselt habe. Grundfarbe grün wie Pantone 2293 C.
Als Anhaltspunkt was derzeit bei im Einsatz ist, habe ich die entsprechenden Dateien hochgeladen.

```html
<!DOCTYPE html>
<html lang="de">
<head>
<meta charset="utf-8">
<title>Steuerberater Konrad Albers – Geschäftsausstattung</title>
<link href="https://fonts.googleapis.com/css2?family=Barlow+Semi+Condensed:wght@400;600&display=swap" rel="stylesheet">
<style>
:root{
  --green:#86c400;
  --ink:#1a1a1a;
  --grey:#666;
  --paper:#fff;
  --blush:#f9ebe8;
  --frame:#cfcfcf;
}
*{margin:0;padding:0;box-sizing:border-box}
html,body{width:973px;height:1200px;overflow:hidden;background:#fff}
body{position:relative;font-family:"Barlow Semi Condensed",sans-serif;color:var(--ink)}
.sheet{position:absolute;background:var(--paper)}
.letterhead{left:217px;top:43px;width:537px;height:760px;box-shadow:0 0 3px rgba(0,0,0,.35)}
.mark{position:absolute;background:var(--green)}
.wordmark{position:absolute;font-weight:600;text-transform:uppercase;color:var(--ink);line-height:1.05;letter-spacing:.06em;white-space:nowrap}
.sender-line{position:absolute;left:64px;top:143px;font-size:6px;color:var(--ink)}
.sender-line .name{color:var(--green);font-weight:600}
.contact-block{position:absolute;left:404px;top:630px;font-size:9px;line-height:10.3px;color:var(--grey)}
.contact-block .name{color:var(--green);font-weight:600;font-size:10px}
.contact-block .role{color:var(--green)}
.contact-block p{margin-bottom:10px}
.green-bar{position:absolute;background:var(--green)}
.card{top:828px;width:120px;height:185px;box-shadow:0 0 2px rgba(0,0,0,.5)}
.card-front{left:254px}
.card-back{left:384px;text-align:center}
.card-back .details{position:absolute;left:0;right:0;top:80px;font-size:5.8px;line-height:7.2px;color:var(--grey)}
.card-back .details .name{color:var(--green);font-weight:600;font-size:6.5px}
.card-back .details .role{color:var(--green)}
.card-back .details p{margin-bottom:7px}
.notepad{left:529px;top:829px;width:184px;height:184px;border:1px solid var(--ink)}
.notepad .header-tint{position:absolute;left:0;top:0;right:0;height:49px;background:var(--blush)}
.notepad .contact{position:absolute;right:8px;top:156px;text-align:right;font-size:5.8px;line-height:7.5px;font-weight:600;color:var(--green)}
.folder{position:absolute;top:1035px;width:52px;height:114px}
.folder-one{left:452px;background:var(--paper);box-shadow:0 0 2px rgba(0,0,0,.4)}
.folder-two{left:518px}
.folder-body{position:absolute;left:0;top:0;width:52px;height:114px}
.folder .wordmark{writing-mode:vertical-lr;left:21px;top:7px;font-size:5px;letter-spacing:.03em;line-height:1.15}
.folder .mark{left:20px;top:61px;width:14px;height:14px}
</style>
</head>
<body>

<section class="sheet letterhead" aria-label="Briefbogen">
  <div class="mark" style="left:403px;top:39px;width:84px;height:84px"></div>
  <div class="wordmark" style="left:403px;top:131px;font-size:8.5px;width:84px">Steuerberater<br>Konrad Albers</div>
  <div class="sender-line"><span class="name">Konrad Albers</span> Steuerberater • Lindenweg 4 • 84102 Talheim</div>
  <div class="contact-block">
    <p><span class="name">Konrad Albers</span><br><span class="role">Steuerberater</span></p>
    <p>Lindenweg 4<br>84102 Talheim</p>
    <p>Tel.: 08921 / 556 12 – 10<br>Fax: 08921 / 556 12 – 11</p>
    <p>info@kanzlei-albers.de<br>www.kanzlei-albers.de</p>
  </div>
  <div class="green-bar" style="left:403px;bottom:0;width:84px;height:10px"></div>
</section>

<section class="sheet card card-front" aria-label="Visitenkarte Vorderseite">
  <div class="mark" style="left:0;top:0;width:120px;height:120px"></div>
  <div class="wordmark" style="left:16px;top:140px;font-size:8.5px">Steuerberater<br>Konrad Albers</div>
  <div class="green-bar" style="left:0;bottom:0;width:100%;height:7px"></div>
</section>

<section class="sheet card card-back" aria-label="Visitenkarte Rückseite">
  <div class="mark" style="left:43px;top:19px;width:32px;height:32px"></div>
  <div class="details">
    <p><span class="name">Konrad Albers</span><br><span class="role">Steuerberater</span></p>
    <p>Lindenweg 4<br>84102 Talheim</p>
    <p>Tel.: 08921 / 556 12 – 10<br>Fax: 08921 / 556 12 – 11</p>
    <p>info@kanzlei-albers.de<br>www.kanzlei-albers.de</p>
  </div>
  <div class="green-bar" style="left:0;bottom:0;width:100%;height:7px"></div>
</section>

<section class="sheet notepad" aria-label="Notizblock">
  <div class="header-tint"></div>
  <div class="mark" style="left:7px;top:147px;width:23px;height:23px"></div>
  <div class="wordmark" style="left:36px;top:152px;font-size:7.5px">Steuerberater<br>Konrad Albers</div>
  <div class="contact">08921 / 556 12 – 10<br>www.kanzlei-albers.de</div>
  <div class="green-bar" style="left:0;bottom:0;width:100%;height:8px"></div>
</section>

<section class="folder folder-one" aria-label="Bindemappe">
  <div class="green-bar" style="left:0;top:0;width:7px;height:100%"></div>
  <div class="green-bar" style="right:0;top:0;width:6px;height:100%"></div>
  <div class="wordmark">Steuerberater<br>Konrad Albers</div>
  <div class="mark"></div>
</section>

<section class="folder folder-two" aria-label="Bindemappe mit Eckschnitt">
  <svg class="folder-body" viewBox="0 0 52 114" width="52" height="114" aria-hidden="true">
    <polygon points="4,0.5 51.5,0.5 51.5,71 7,113.5 4,113.5 0.5,110 0.5,4" fill="#fff" stroke="#cfcfcf" stroke-width="1"/>
    <polygon points="4,0 7,0 7,114 4,114 0,110 0,4" fill="#86c400"/>
    <polygon points="46,0 52,0 52,70.5 46,76.5" fill="#86c400"/>
  </svg>
  <div class="wordmark">Steuerberater<br>Konrad Albers</div>
  <div class="mark"></div>
</section>

</body>
</html>
```